Plakate für Haushaltshilfen und Alltagsbegleiter
Zielgruppe
Wir bieten haushaltsnahe Dienstleistungen (Haushaltshilfen und Altgasbegleiter) für Personen mit einem Pflegegrad 1 - 5 an.
Zielgruppe sind Personen mit einem Pflegegrad 1 - 5. Hauptsächlich ältere Menschen die Unterstützung/Betreuung im Alltag und Haushalt benötigen.
Aufgabenstellung
Wir benötigen für unsere Büroräume eine Fensterbeschriftung. Es handelt sich hier um 5 Fenster (Glasflächen) und eine Glastür. Die Vorgabe ist, dass von außen zu erkennen ist dass sich um alle Räumlichkeiten um unsere (Firma Lindwerk) Räumlichkeiten handelt. Desweiteren soll auch unser Angebot erkennbar sein.
Unser Angebot enthält: Haushaltshilfen und Alltagsbegleiter
- kostenlose Haushaltshilfe ab Pflegegrad 1
- Abrechnung mit allen Kostenträgern
Da wir keine Schilder an die Fassade anbringen können, müßen die Glasflächen dafür genutzt werden um zum Einen uns als Firma erkennbar zu machen und zum anderen unser Angebot kurz zu präsentieren.
Uns ist wichtig dass unser Logo verwendet wir und auch unsere Farben.
Desweiteren sollten an den Fenstern auch teilweise eine Sichtschutz nach innen, angebracht werden, aber eben nur teilweise also nicht das ganzen Fenster z.Bsp. mit einer Blickdichten Folie überziehen, sondern in Augenhöhe wenn Fußgänger vorbei laufen.

```html
<!DOCTYPE html>
<html lang="de">
<head>
<meta charset="utf-8">
<title>Lindwerk – Fensterplakate</title>
<link href="https://fonts.googleapis.com/css2?family=Montserrat:wght@400;600;800&display=swap" rel="stylesheet">
<style>
:root{
  --red:#c8242a;
  --red-dark:#9e1a1f;
  --charcoal:#323232;
  --slate:#5b5b5b;
  --stage:#646464;
  --paper:#e6e6e6;
  --white:#ffffff;
  --ink:#3a3a3a;
}
*{margin:0;padding:0;box-sizing:border-box}
html,body{width:1200px;height:733px;overflow:hidden}
body{background:var(--stage);font-family:"Montserrat",sans-serif;position:relative}
.poster{position:absolute;overflow:hidden}
.poster svg.bands{position:absolute;left:0;top:0;width:100%;height:100%}
.photo{position:absolute}
.brand{position:absolute;display:flex;align-items:center;gap:5px}
.brand-dot{width:22px;height:22px;border-radius:50%;border:2.5px solid var(--red);flex:none}
.brand-name{font-weight:600;font-size:15px;letter-spacing:1px;color:var(--ink);line-height:1}
.brand-tag{font-size:5px;letter-spacing:.5px;color:var(--red);text-transform:uppercase;margin-top:2px}
.brand.light .brand-name{color:var(--white)}
.brand.light .brand-dot{border-color:var(--white)}
.brand.light .brand-tag{color:var(--white)}
.brand.stacked{flex-direction:column;gap:3px;left:0;right:0;text-align:center}
.tag{position:absolute;background:var(--red);color:var(--white);font-weight:800;font-size:7px;line-height:1.2;text-transform:uppercase;padding:4px 8px;border-radius:3px;text-align:center}

/* Plakat 1 – Vorteile */
.p-benefits{left:16px;top:254px;width:188px;height:255px;background:linear-gradient(180deg,#ededed,#d9d9d9)}
.benefit-bar{position:absolute;left:0;right:0;top:77px;height:17px;background:var(--charcoal);color:var(--white);font-weight:800;font-size:10px;text-align:center;line-height:17px}
.benefits{position:absolute;left:8px;right:8px;top:103px;display:grid;grid-template-columns:1fr 1fr;row-gap:10px}
.benefit{text-align:center;font-size:5.4px;color:var(--ink);line-height:1.25}
.benefit-icon{width:29px;height:29px;margin:0 auto 3px;background:var(--red);border-radius:4px;display:flex;align-items:center;justify-content:center}

/* Plakat 2 – Angebot */
.p-offer{left:220px;top:254px;width:188px;height:255px;background:var(--paper)}
.offer-text{position:absolute;left:0;right:0;bottom:12px;color:var(--white);font-weight:800;font-size:8.6px;line-height:1.4;text-align:center;text-transform:uppercase}

/* Plakat 3 – Haushaltshilfen */
.p-help{left:424px;top:254px;width:188px;height:255px;background:var(--paper)}
.help-title{position:absolute;left:0;right:0;top:80px;color:var(--red);font-weight:800;font-size:10px;line-height:1.35;text-align:center;text-transform:uppercase}

/* Plakat 4 – Kostenträger */
.p-billing{left:628px;top:231px;width:188px;height:303px;background:var(--charcoal)}

/* Plakat 5 – Glastür */
.p-door{left:832px;top:200px;width:148px;height:332px;background:var(--slate)}
.door-text{position:absolute;left:10px;right:8px;top:123px;color:var(--white);font-weight:800;font-size:7.4px;line-height:1.4;text-transform:uppercase}

/* Plakat 6 – Kontakt */
.p-contact{left:996px;top:231px;width:188px;height:303px;background:var(--charcoal)}
.contact-lead{position:absolute;left:0;right:0;top:200px;color:var(--white);font-size:9px;text-align:center}
.contact-phone{position:absolute;left:17px;right:17px;top:222px;height:21px;background:var(--red);border-radius:6px;color:var(--white);font-weight:800;font-size:13px;text-align:center;line-height:21px;letter-spacing:.5px}
.contact-web{position:absolute;left:0;right:0;top:251px;color:var(--white);font-weight:600;font-size:13px;text-align:center}
</style>
</head>
<body>

<!-- Plakat 1 -->
<section class="poster p-benefits">
  <svg class="bands" viewBox="0 0 188 255" preserveAspectRatio="none">
    <polygon points="0,219 60,235 188,200 188,255 0,255" fill="var(--red)"/>
    <polygon points="90,255 188,222 188,255" fill="var(--charcoal)"/>
  </svg>
  <div class="brand stacked" style="top:8px">
    <span class="brand-dot" style="width:30px;height:30px"></span>
    <div><div class="brand-name" style="font-size:13px">LINDWERK</div><div class="brand-tag">Haushaltshilfen &amp; mehr</div></div>
  </div>
  <div class="benefit-bar">UNSERE VORTEILE</div>
  <div class="benefits">
    <div class="benefit"><div class="benefit-icon"><svg width="14" height="16" viewBox="0 0 14 16"><rect x="1" y="1" width="12" height="14" rx="1" fill="none" stroke="#fff" stroke-width="1.6"/><line x1="4" y1="5" x2="10" y2="5" stroke="#fff" stroke-width="1.4"/><line x1="4" y1="9" x2="10" y2="9" stroke="#fff" stroke-width="1.4"/></svg></div>Abrechnung mit allen Pflegekassen möglich</div>
    <div class="benefit"><div class="benefit-icon"><svg width="16" height="16" viewBox="0 0 16 16"><path d="M8 2v8M4 6h8" stroke="#fff" stroke-width="2"/><path d="M1 13h14" stroke="#fff" stroke-width="2"/></svg></div>Abrechnung über den Entlastungsbetrag von mind. 125 € mtl. ab Pflegegrad 1 möglich</div>
    <div class="benefit"><div class="benefit-icon"><svg width="16" height="16" viewBox="0 0 16 16"><path d="M8 10 4 6a2 2 0 0 1 4-2 2 2 0 0 1 4 2z" fill="#fff"/><path d="M1 13h14" stroke="#fff" stroke-width="2"/></svg></div>Auch über die Verhinderungspflege</div>
    <div class="benefit"><div class="benefit-icon"><svg width="14" height="16" viewBox="0 0 14 16"><rect x="1" y="1" width="10" height="14" rx="1" fill="none" stroke="#fff" stroke-width="1.6"/><path d="M5 11l7-8" stroke="#fff" stroke-width="1.8"/></svg></div>Hilfe bei der Antragsstellung</div>
  </div>
</section>

<!-- Plakat 2 -->
<section class="poster p-offer">
  <div class="photo" role="img" aria-label="Schwarz-weiß-Foto: Hände einer helfenden Person auf den Händen eines älteren Menschen am Gehstock" style="left:0;top:40px;width:188px;height:160px;background:radial-gradient(ellipse at 55% 55%,#9a9a9a,#cfcfcf 60%,#e6e6e6)"></div>
  <svg class="bands" viewBox="0 0 188 255" preserveAspectRatio="none">
    <polygon points="0,180 70,170 140,192 188,160 188,255 0,255" fill="var(--red)"/>
    <polygon points="0,200 70,183 140,205 188,182 188,255 0,255" fill="var(--charcoal)"/>
  </svg>
  <div class="brand" style="left:18px;top:18px">
    <span class="brand-dot" style="width:26px;height:26px"></span>
    <div><div class="brand-name" style="font-size:16px">LINDWERK</div><div class="brand-tag">Haushaltshilfen &amp; mehr</div></div>
  </div>
  <p class="offer-text">Wir bieten Haushaltshilfen<br>und Alltagsbegleiter für<br>Privathaushalte an.</p>
</section>

<!-- Plakat 3 -->
<section class="poster p-help">
  <div class="photo" role="img" aria-label="Schwarz-weiß-Foto: Person wischt den Boden eines hellen Wohnzimmers" style="left:0;top:112px;width:188px;height:143px;background:linear-gradient(180deg,#e9e9e9,#bdbdbd 70%,#d4d4d4)"></div>
  <svg class="bands" viewBox="0 0 188 255" preserveAspectRatio="none">
    <polygon points="0,0 85,0 0,40" fill="var(--red)"/>
    <polygon points="85,0 188,0 188,40 130,20" fill="var(--charcoal)"/>
  </svg>
  <div class="brand stacked" style="top:12px">
    <span class="brand-dot" style="width:32px;height:32px"></span>
    <div><div class="brand-name" style="font-size:13px">LINDWERK</div><div class="brand-tag">Haushaltshilfen &amp; mehr</div></div>
  </div>
  <p class="help-title">Haushaltshilfen und<br>Alltagsbegleiter</p>
  <div class="tag" style="left:12px;top:194px;transform:rotate(8deg);font-size:6.8px;text-align:left">Kostenlose<br>Haushaltshilfe<br>ab Pflegegrad 1</div>
</section>

<!-- Plakat 4 -->
<section class="poster p-billing">
  <div class="photo" role="img" aria-label="Schwarz-weiß-Foto: älteres Paar geht Arm in Arm, von hinten gesehen" style="left:0;top:90px;width:188px;height:213px;background:radial-gradient(ellipse at 50% 60%,#6c6c6c,#a8a8a8 55%,#cfcfcf)"></div>
  <svg class="bands" viewBox="0 0 188 303" preserveAspectRatio="none">
    <polygon points="0,68 60,62 150,100 188,78 188,108 150,112 60,78 0,103" fill="var(--red)"/>
  </svg>
  <div class="brand light" style="left:18px;top:18px">
    <span class="brand-dot" style="width:32px;height:32px"></span>
    <div><div class="brand-name" style="font-size:17px">LINDWERK</div><div class="brand-tag">Haushaltshilfen &amp; mehr</div></div>
  </div>
  <div class="tag" style="left:76px;top:244px;transform:rotate(-10deg)">Abrechnung mit<br>allen<br>Kostenträgern</div>
</section>

<!-- Plakat 5 -->
<section class="poster p-door">
  <svg class="bands" viewBox="0 0 148 332" preserveAspectRatio="none">
    <polygon points="0,0 115,0 0,72" fill="var(--red)"/>
    <polygon points="115,0 148,0 148,40 100,10" fill="var(--white)"/>
    <polygon points="0,280 50,283 110,300 148,278 148,332 0,332" fill="var(--red)"/>
    <polygon points="0,300 60,300 110,318 148,300 148,332 0,332" fill="var(--white)"/>
  </svg>
  <div class="brand light" style="left:10px;top:86px">
    <span class="brand-dot" style="width:26px;height:26px"></span>
    <div><div class="brand-name" style="font-size:13px">LINDWERK</div><div class="brand-tag">Haushaltshilfen &amp; mehr</div></div>
  </div>
  <p class="door-text">Den Alltag zu bewältigen kann eine echte Herausforderung sein. Egal ob Sie Hilfe beim Einkaufen oder anderen alltäglichen Aktivitäten benötigen, wir helfen gerne.</p>
</section>

<!-- Plakat 6 -->
<section class="poster p-contact">
  <div class="photo" role="img" aria-label="Schwarz-weiß-Foto: zwei offene Hände halten ein Papierherz mit zwei älteren Figuren" style="left:0;top:0;width:188px;height:150px;background:radial-gradient(ellipse at 50% 35%,#f2f2f2,#a9a9a9 55%,#d8d8d8)"></div>
  <svg class="bands" viewBox="0 0 188 303" preserveAspectRatio="none">
    <polygon points="0,110 188,110 188,150 0,150" fill="var(--white)"/>
    <polygon points="0,155 60,150 140,170 188,150 188,188 140,198 60,172 0,180" fill="var(--red)"/>
  </svg>
  <div class="brand" style="left:18px;top:118px">
    <span class="brand-dot" style="width:30px;height:30px"></span>
    <div><div class="brand-name" style="font-size:16px">LINDWERK</div><div class="brand-tag">Haushaltshilfen &amp; mehr</div></div>
  </div>
  <p class="contact-lead">Buchen Sie gleich einen Termin:</p>
  <div class="contact-phone">0711 98 76 54 32</div>
  <p class="contact-web">www.lindwerk.de</p>
</section>

</body>
</html>
```